Workplace Safety Consultancy Business needs business card design

We need a business card for a new business providing workplace health and safety consulting called 'Worksure Path'. We will be providing small to medium sized businesses assistance with OH&S and HR matters to ensure that their employees and the public are safe in the workplace and that they are meeting their legislative requirements. Would like to see the words 'practical workplace safety solutions' on the card. Personal details on the back. It needs to be clean, smart and professional (no fluff). Would like to see a simple logo if possible as well. Have been looking at orange and black, but open to other ideas.
Updates
Thank you to those to have created designs for us so far! We are really impressed with the impact of the black and orange having now seen it. Would be great if any further designs used those colours. Cheers.

Thank you to everyone that submitted a design. Your work is of the highest quality and we had a hard decision deciding. Sorry if we didn't choose your design, but it just came down to the one that stood out to us personally. Cheers.

Target Market(s)
Small-Medium business owners in Queensland, Australia. Age 25-60 male and female. Initially targeting those in the trade type industries
Industry/Entity Type
Health
Look and feel
Each slider illustrates characteristics of the customer's brand and the style your logo design should communicate.

```html
<!DOCTYPE html>
<html lang="en">
<head>
<meta charset="utf-8">
<title>Worksure Path – Business Card</title>
<link href="https://fonts.googleapis.com/css2?family=Exo+2:wght@400;600&display=swap" rel="stylesheet">
<style>
  :root {
    --backdrop: #b9babd;
    --card: #161616;
    --accent: #f7a21b;
    --text-light: #f2f2f2;
    --text-muted: #cfcfcf;
  }
  * { margin: 0; padding: 0; box-sizing: border-box; }
  html, body {
    width: 1200px; height: 900px; overflow: hidden;
    background: var(--backdrop);
    font-family: "Exo 2", "Segoe UI", sans-serif;
  }
  .sheet {
    width: 1200px; height: 900px;
    display: flex; flex-direction: column; align-items: center; justify-content: center;
    gap: 44px;
  }
  .card {
    position: relative;
    width: 620px; height: 354px;
    background: var(--card);
    border-radius: 30px;
    overflow: hidden;
    box-shadow: 0 10px 24px rgba(0,0,0,.25);
  }
  .rule { position: absolute; height: 7px; background: var(--accent); }

  /* front */
  .card--front .brand {
    position: absolute; right: 34px; top: 188px;
    font-size: 40px; font-weight: 600; letter-spacing: .5px;
    color: var(--accent); line-height: 1; text-transform: uppercase;
  }
  .card--front .tagline {
    position: absolute; right: 34px; top: 236px;
    font-size: 17px; font-weight: 400; color: var(--text-light); line-height: 1;
  }
  .tagline .hl { color: var(--accent); }
  .card--front .rule { left: 0; top: 250px; width: 322px; }

  /* back */
  .card--back .brand {
    position: absolute; left: 36px; top: 96px;
    font-size: 40px; font-weight: 600; letter-spacing: .5px;
    color: var(--accent); line-height: 1; text-transform: uppercase;
  }
  .card--back .rule--upper { left: 360px; right: 0; top: 118px; }
  .card--back .rule--lower { left: 0; right: 0; top: 322px; }
  .holder {
    position: absolute; left: 36px; top: 188px;
    font-size: 22px; font-weight: 600; color: var(--accent);
    text-transform: uppercase; letter-spacing: .3px;
  }
  .contacts {
    position: absolute; left: 36px; top: 224px;
    list-style: none; display: flex; flex-direction: column; gap: 7px;
  }
  .contacts li {
    display: flex; align-items: center; gap: 10px;
    font-size: 16px; color: var(--text-muted);
  }
  .contacts svg { width: 18px; height: 18px; flex: none; }
</style>
</head>
<body>
<main class="sheet">

  <section class="card card--front" aria-label="Card front">
    <div class="brand">Worksure Path</div>
    <div class="rule"></div>
    <div class="tagline">practical workplace <span class="hl">safety</span> solutions</div>
  </section>

  <section class="card card--back" aria-label="Card back">
    <div class="brand">Worksure Path</div>
    <div class="rule rule--upper"></div>
    <div class="holder">Daniel Cartwright</div>
    <ul class="contacts">
      <li>
        <svg viewBox="0 0 18 18" aria-hidden="true"><rect width="18" height="18" rx="2" fill="#f7a21b"/><rect x="6" y="3" width="6" height="12" rx="1" fill="none" stroke="#161616" stroke-width="1.6"/><circle cx="9" cy="12.5" r=".9" fill="#161616"/></svg>
        0400 555 012
      </li>
      <li>
        <svg viewBox="0 0 18 18" aria-hidden="true"><rect width="18" height="18" rx="2" fill="#f7a21b"/><rect x="3.5" y="5" width="11" height="8" fill="none" stroke="#161616" stroke-width="1.5"/><path d="M3.5 5 9 10l5.5-5" fill="none" stroke="#161616" stroke-width="1.5"/></svg>
        daniel@worksurepath.net.au
      </li>
      <li>
        <svg viewBox="0 0 18 18" aria-hidden="true"><rect width="18" height="18" rx="2" fill="#f7a21b"/><circle cx="9" cy="9" r="5.5" fill="none" stroke="#161616" stroke-width="1.5"/><ellipse cx="9" cy="9" rx="2.3" ry="5.5" fill="none" stroke="#161616" stroke-width="1.2"/><path d="M3.5 9h11" stroke="#161616" stroke-width="1.2"/></svg>
        www.worksurepath.net.au
      </li>
    </ul>
    <div class="rule rule--lower"></div>
  </section>

</main>
</body>
</html>
```